Fernhollow Ridge Farms
letterhead, envelope and business cards
Fernhollow Ridge Farms -
Creative Brief
Traditional
Tessa Harlan
3157 W Birch Mill Road North Platte, NE 68437
sales@fernhollowridgefarms.example
www.fernhollowridgefarms.example

```html
<!DOCTYPE html>
<html lang="en">
<head>
<meta charset="utf-8">
<title>Fernhollow Ridge Farms – Stationery</title>
<link href="https://fonts.googleapis.com/css2?family=Cormorant+Garamond:wght@500;600&family=Lato:wght@400&display=swap" rel="stylesheet">
<style>
  :root {
    --bg: #ffffff;
    --paper: #ffffff;
    --edge: #d9d9d9;
    --brown: #5b3b22;
    --tan: #c7b096;
    --tan-dark: #a98c6d;
    --cream: #f6f1ea;
    --ghost: #efe8df;
    --ghost-art: #f3eee7;
    --ink: #8a8078;
    --divider: #d8cfc5;
  }
  * { margin: 0; padding: 0; box-sizing: border-box; }
  html, body { width: 1200px; height: 908px; overflow: hidden; background: var(--bg); }
  .canvas { position: relative; width: 1200px; height: 908px; }

  .brand {
    font-family: "Cormorant Garamond", Georgia, serif;
    font-weight: 600;
    color: var(--brown);
    line-height: 0.95;
    text-align: center;
  }
  .small-print {
    font-family: "Lato", Arial, sans-serif;
    font-size: 6.5px;
    letter-spacing: 0.08em;
    color: var(--ink);
    line-height: 1.55;
  }

  /* Letterhead */
  .letterhead {
    position: absolute; left: 228px; top: 43px; width: 607px; height: 802px;
    background: var(--paper); border: 1px solid var(--edge);
    box-shadow: 0 1px 3px rgba(0,0,0,0.08);
  }
  .letterhead .brand { position: absolute; left: 14px; top: 40px; width: 210px; font-size: 30px; }
  .letterhead .divider { position: absolute; left: 234px; top: 28px; width: 1px; height: 130px; background: var(--divider); }
  .letterhead .small-print { position: absolute; left: 242px; top: 96px; }
  .letterhead .ghost-art {
    position: absolute; left: 40px; top: 500px; width: 560px; height: 210px;
    background: radial-gradient(ellipse at 50% 70%, var(--ghost-art), rgba(255,255,255,0));
  }
  .letterhead .ghost-name {
    position: absolute; left: 0; bottom: -12px; width: 100%;
    font-family: "Cormorant Garamond", Georgia, serif; font-weight: 500;
    font-size: 118px; color: var(--ghost); text-align: center; white-space: nowrap;
  }

  /* Envelope */
  .envelope {
    position: absolute; left: 65px; top: 240px; width: 648px; height: 288px;
    background: var(--paper); border: 1px solid var(--edge);
    box-shadow: 0 1px 3px rgba(0,0,0,0.1);
  }
  .envelope .brand { position: absolute; left: 10px; top: 34px; width: 168px; font-size: 23px; }
  .envelope .divider { position: absolute; left: 182px; top: 18px; width: 1px; height: 100px; background: var(--divider); }
  .envelope .small-print { position: absolute; left: 194px; top: 86px; }

  /* Business cards */
  .card {
    position: absolute; left: 859px; width: 252px; height: 143px;
    border-radius: 10px; overflow: hidden;
  }
  .card-front {
    top: 228px;
    background: linear-gradient(180deg, var(--cream) 0%, var(--tan) 45%, var(--tan-dark) 100%);
  }
  .card-front .brand {
    position: absolute; left: 0; top: 30px; width: 100%; font-size: 40px;
  }
  .card-back {
    top: 384px; height: 140px;
    background: var(--paper); border: 1px solid var(--edge);
  }
  .card-back .brand { position: absolute; left: 8px; top: 26px; width: 120px; font-size: 17px; }
  .card-back .divider { position: absolute; left: 134px; top: 12px; width: 1px; height: 72px; background: var(--divider); }
  .card-back .holder {
    position: absolute; left: 150px; top: 28px;
    font-family: "Cormorant Garamond", Georgia, serif; font-weight: 600;
    font-size: 15px; letter-spacing: 0.12em; color: var(--brown);
  }
  .card-back .small-print { position: absolute; left: 0; top: 94px; width: 100%; text-align: center; font-size: 6px; }
</style>
</head>
<body>
<div class="canvas">

  <section class="letterhead">
    <div class="brand">Fernhollow<br>Ridge Farms</div>
    <div class="divider"></div>
    <address class="small-print" style="font-style:normal">
      3157 W Birch Mill Road<br>
      North Platte, NE 68437<br>
      Phone: 308.555.0142<br>
      Email: sales@fernhollowridgefarms.example<br>
      www.fernhollowridgefarms.example
    </address>
    <div class="ghost-art" role="img" aria-label="Faint farm illustration with birds, dog and flourishes as a watermark backdrop"></div>
    <div class="ghost-name">Fernhollow</div>
  </section>

  <section class="envelope">
    <div class="brand">Fernhollow<br>Ridge Farms</div>
    <div class="divider"></div>
    <address class="small-print" style="font-style:normal">
      3157 W Birch Mill Road<br>
      North Platte, NE 68437
    </address>
  </section>

  <section class="card card-front" role="img" aria-label="Business card front with soft farm scene backdrop and company name">
    <div class="brand">Fernhollow<br>Ridge Farms</div>
  </section>

  <section class="card card-back">
    <div class="brand">Fernhollow<br>Ridge Farms</div>
    <div class="divider"></div>
    <div class="holder">TESSA HARLAN</div>
    <address class="small-print" style="font-style:normal">
      3157 W Birch Mill Road North Platte, NE 68437<br>
      Phone: 308.555.0142<br>
      Email: sales@fernhollowridgefarms.example<br>
      www.fernhollowridgefarms.example
    </address>
  </section>

</div>
</body>
</html>
```